Frostvale Climate Crew WA Truck

I want a truck desing that screams Professional, Friendly and serious about work. you can find some of our work on our website, facebook and instagram.
https://frostvalecrew.example.com.au/
https://www.instagram.com/frostvalecrew.example/
https://www.facebook.com/frostvalecrew.example/

The design needs to include our refrigeration license: AU38452 and electrical License: EC94031
I want the colours to be consistent with my Logo.

Key Notes to be included in the design, I want to let people know we do the following;
- Commercial and Residential
- Repairs, Service and Installation
- Reverse cycle ducted Air Conditioning
- Wall Split Air Conditioning
- Ceiling Cassettes
- Evaporative Air Conditioning
- Cool Rooms
- Display Fridges
- Beer Chillers

```html
<!DOCTYPE html>
<html lang="en">
<head>
<meta charset="utf-8">
<title>Frostvale Climate Crew WA – Truck Wrap</title>
<link href="https://fonts.googleapis.com/css2?family=Poppins:wght@400;500;600;800&display=swap" rel="stylesheet">
<style>
  :root{
    --navy:#0d3a7a;
    --blue:#1f6fd1;
    --sky:#5fa8ee;
    --ice:#eaf3fc;
    --white:#ffffff;
    --orange:#f07a1e;
    --red:#e0262a;
    --stage:#d9dee5;
  }
  *{box-sizing:border-box;margin:0;padding:0}
  html,body{width:1200px;height:859px;overflow:hidden;background:var(--stage);font-family:"Poppins",sans-serif;color:var(--navy)}
  .wrap{position:relative;width:1200px;height:859px}

  .panel{position:absolute;overflow:hidden;background:linear-gradient(180deg,var(--white) 0%,var(--ice) 100%);box-shadow:0 2px 8px rgba(0,0,0,.18)}
  .panel-wave{position:absolute;left:0;right:0;bottom:0;height:70%;
    background:linear-gradient(165deg,rgba(95,168,238,0) 0%,rgba(95,168,238,.45) 45%,var(--blue) 100%)}

  /* side panel */
  .side{left:20px;top:20px;width:1160px;height:450px}
  .side .licences{position:absolute;right:28px;top:16px;font-size:15px;font-weight:500;display:flex;gap:34px;z-index:1}
  .licences b,.door-licence b{color:var(--red);font-weight:600}
  .side .headline{position:absolute;left:400px;right:28px;top:48px;font-size:40px;line-height:1.18;font-weight:800;text-align:center;z-index:1}
  .brand{display:flex;align-items:center;gap:10px;font-weight:800;color:var(--navy);line-height:1.1;z-index:1}
  .brand-dot{flex:none;border-radius:50%;background:var(--orange)}
  .side .brand{position:absolute;left:30px;top:60px;width:340px;font-size:30px}
  .side .brand-dot{width:38px;height:38px}
  .side .contact{position:absolute;left:30px;bottom:40px;font-size:15px;color:var(--white);font-weight:500;line-height:1.8;z-index:1}
  .contact-row{display:flex;align-items:center;gap:8px;white-space:nowrap}
  .contact-row svg{width:16px;height:16px;flex:none}

  .services{position:absolute;left:400px;right:40px;top:160px;display:grid;grid-template-columns:repeat(3,1fr);gap:16px 22px;z-index:1}
  .service{display:flex;align-items:center;gap:12px;height:78px;padding:0 16px;background:rgba(255,255,255,.82);border-radius:6px;font-size:16px;font-weight:500;color:var(--navy);line-height:1.25}
  .service-mark{flex:none;width:22px;height:22px;border-radius:4px;background:linear-gradient(135deg,var(--orange),var(--red))}

  /* rear doors */
  .door{top:490px;width:290px;height:350px}
  .door-left{left:305px}
  .door-right{left:605px}
  .door > *{position:absolute}
  .door-licence{left:0;right:0;top:16px;text-align:center;font-size:14px;font-weight:500;z-index:1}
  .door .brand{left:20px;right:20px;top:74px;font-size:21px;justify-content:center}
  .door .brand-dot{width:28px;height:28px}
  .door-left .tagline{left:12px;right:12px;top:162px;text-align:center;font-size:16px;font-weight:600;line-height:1.35;z-index:1}
  .door-right .phone{left:0;right:0;top:150px;display:flex;justify-content:center;align-items:center;gap:8px;font-size:25px;font-weight:600;z-index:1}
  .door-right .phone svg{width:24px;height:24px}
  .door-right .details{left:14px;right:8px;top:196px;font-size:10px;font-weight:500;line-height:1.9;z-index:1}
  .door-right .contact-row{gap:5px}
  .door-right .contact-row svg{width:10px;height:10px}
  .door-seam{position:absolute;top:490px;left:597px;width:6px;height:350px;background:#9aa3ad}
</style>
</head>
<body>
<div class="wrap">

  <section class="panel side" aria-label="Truck side panel">
    <div class="panel-wave" role="img" aria-label="Flowing blue wave and snowflake backdrop"></div>
    <div class="licences">
      <span>Refrigeration License: <b>AU38452</b></span>
      <span>Electrical License: <b>EC94031</b></span>
    </div>
    <div class="brand"><span class="brand-dot"></span><span>Frostvale<br>Climate Crew WA</span></div>
    <h1 class="headline">Commercial &amp; Residential<br>Air Conditioning Specialists</h1>
    <div class="services">
      <div class="service"><span class="service-mark"></span>Commercial and Residential</div>
      <div class="service"><span class="service-mark"></span>Repairs, Service and Installation</div>
      <div class="service"><span class="service-mark"></span>Reverse cycle ducted Air Conditioning</div>
      <div class="service"><span class="service-mark"></span>Wall Split Air Conditioning</div>
      <div class="service"><span class="service-mark"></span>Ceiling Cassettes</div>
      <div class="service"><span class="service-mark"></span>Evaporative Air Conditioning</div>
      <div class="service"><span class="service-mark"></span>Cool Rooms</div>
      <div class="service"><span class="service-mark"></span>Display Fridges</div>
      <div class="service"><span class="service-mark"></span>Beer Chillers</div>
    </div>
    <div class="contact">
      <div class="contact-row"><svg viewBox="0 0 24 24" fill="currentColor"><path d="M6.6 10.8a15 15 0 0 0 6.6 6.6l2.2-2.2a1 1 0 0 1 1-.25 11.4 11.4 0 0 0 3.6.57 1 1 0 0 1 1 1V20a1 1 0 0 1-1 1A17 17 0 0 1 3 4a1 1 0 0 1 1-1h3.5a1 1 0 0 1 1 1c0 1.25.2 2.45.57 3.57a1 1 0 0 1-.25 1z"/></svg>0491 570 156</div>
      <div class="contact-row"><svg viewBox="0 0 24 24" fill="currentColor"><path d="M3 5h18v14H3zm2 2v.5l7 4.5 7-4.5V7z"/></svg>info@frostvalecrew.example.com.au</div>
      <div class="contact-row"><svg viewBox="0 0 24 24" fill="none" stroke="currentColor" stroke-width="2"><circle cx="12" cy="12" r="9"/><path d="M3 12h18M12 3c3 3.5 3 14.5 0 18M12 3c-3 3.5-3 14.5 0 18"/></svg>www.frostvalecrew.example.com.au</div>
    </div>
  </section>

  <section class="panel door door-left" aria-label="Rear left door">
    <div class="panel-wave" role="img" aria-label="Flowing blue wave and snowflake backdrop"></div>
    <p class="door-licence">Refrigeration License: <b>AU38452</b></p>
    <div class="brand"><span class="brand-dot"></span><span>Frostvale<br>Climate Crew WA</span></div>
    <p class="tagline">Commercial &amp; Residential<br>Air Conditioning Specialists</p>
  </section>

  <div class="door-seam"></div>

  <section class="panel door door-right" aria-label="Rear right door">
    <div class="panel-wave" role="img" aria-label="Flowing blue wave and snowflake backdrop"></div>
    <p class="door-licence">Electrical License: <b>EC94031</b></p>
    <div class="brand"><span class="brand-dot"></span><span>Frostvale<br>Climate Crew WA</span></div>
    <div class="phone"><svg viewBox="0 0 24 24" fill="currentColor"><path d="M6.6 10.8a15 15 0 0 0 6.6 6.6l2.2-2.2a1 1 0 0 1 1-.25 11.4 11.4 0 0 0 3.6.57 1 1 0 0 1 1 1V20a1 1 0 0 1-1 1A17 17 0 0 1 3 4a1 1 0 0 1 1-1h3.5a1 1 0 0 1 1 1c0 1.25.2 2.45.57 3.57a1 1 0 0 1-.25 1z"/></svg>0491 570 156</div>
    <div class="details">
      <div class="contact-row"><svg viewBox="0 0 24 24" fill="currentColor"><path d="M3 5h18v14H3zm2 2v.5l7 4.5 7-4.5V7z"/></svg>Email Us : info@frostvalecrew.example.com.au</div>
      <div class="contact-row"><svg viewBox="0 0 24 24" fill="none" stroke="currentColor" stroke-width="2"><circle cx="12" cy="12" r="9"/><path d="M3 12h18M12 3c3 3.5 3 14.5 0 18M12 3c-3 3.5-3 14.5 0 18"/></svg>Website : www.frostvalecrew.example.com.au</div>
    </div>
  </section>

</div>
</body>
</html>
```